I need a website built for my modeling agency company.

On our website, a user can create a profile and we will submit it to thousands of modeling agents throughout the country.

In many cases, they will receive multiple offers from modeling agencies which allows them to pick and choose the contract that is best for them to launch their modeling career.

Some tag lines to consider using:

"Submit your profile to hundreds of modeling agents instantly!"

"Get found and become a star!"

We are: The Runway Guild.

Our Slogan: The World''s Largest Network of Fashion Models and Agents

What We Do: We are an agency with one of the largest networks of fashion professionals that are looking for new modeling talent. We host professional profiles for aspiring models, professional fashion models seeking work, modeling talent seekers, and top modeling agencies. We connect aspiring models with the top modeling agencies in the United States and abroad.

By submitting your FREE profile, you will be instantly introduced to the industry’s leading modeling agents. Within a few days, you could receive multiple, competing offers from modeling agencies that all want to launch your modeling career. Receiving multiple signing offers puts you in control of deciding which contract best suites you!

Reason: I've seen some good designs, but none that are 100% perfect. These are the ones that I like best so far (to give you some ideas): http://files.pixelvane.example/img/510372/820114/820114_4917263_510372_image.jpg http://files.pixelvane.example/img/510372/829305/829305_4926851_510372_image.jpg http://files.pixelvane.example/img/510372/51847/51847_4924097_510372_image.jpg http://files.pixelvane.example/img/510372/51847/51847_4919856_510372_image.jpg http://files.pixelvane.example/img/510372/823670/823670_4920438_510372_image.jpg

Target Market(s)

Aspiring models (mostly female, but some male)

Industry/Entity Type

Modeling Agency

Colors

Designer to choose colors to be used in the design.

Requirements
Nice to have
• Somewhere in the top half of the page, I would like there to be a small form for the visitor to fill out. This form will look as follows:

Title: Instantly contact hundreds of modeling agents who are looking for new talent and could make you a star!
Fields: First Name*, Last Name*, Age, Zip Code, Email Address*, Daytime Phone, Evening Phone, Comments.

Then, there will be a "submit" button to proceed to next step of form. Just below the "submit" button, should be the following verbiage: "You will have the opportunity to upload photo(s) and provide other pertinent information in next step."

```html
<!DOCTYPE html>
<html lang="en">
<head>
<meta charset="utf-8">
<title>The Runway Guild — Get Found &amp; Become a Star</title>
<link href="https://fonts.googleapis.com/css2?family=Gelasio:wght@700&family=Roboto:ital,wght@0,300;0,400;1,400&family=Tinos:wght@700&display=swap" rel="stylesheet">
<style>
  :root {
    --ink: #000000;
    --bar: #050505;
    --text-dark: #1c1c1c;
    --white: #ffffff;
    --panel: rgba(38, 38, 38, 0.86);
    --accent: #ff1a2b;
    --field-text: #333333;
    --photo-light: #c9c9c9;
    --photo-mid: #8f8f8f;
    --photo-dark: #3a3a3a;
  }
  * { box-sizing: border-box; margin: 0; padding: 0; }
  html, body { width: 1200px; height: 1040px; overflow: hidden; background: var(--ink); }
  .page { position: relative; width: 1200px; height: 1040px; overflow: hidden; font-family: 'Roboto', Arial, sans-serif; }

  .site-header {
    position: absolute; left: 0; top: 0; width: 1200px; height: 65px;
    background: var(--bar); display: flex; flex-direction: column;
    align-items: center; justify-content: center; gap: 3px;
  }
  .brand { display: flex; align-items: center; gap: 8px; }
  .brand-mark { width: 14px; height: 14px; background: var(--accent); }
  .brand-name { font-family: 'Roboto', Arial, sans-serif; font-weight: 400; font-size: 20px; color: var(--white); letter-spacing: 0.5px; }
  .brand-slogan { font-size: 7px; color: var(--white); letter-spacing: 0.1px; }

  .hero-photo {
    position: absolute; left: 0; top: 65px; width: 1200px; height: 937px;
    background:
      radial-gradient(ellipse at 80% 35%, var(--photo-light) 0%, var(--photo-mid) 45%, transparent 75%),
      linear-gradient(100deg, #d2d2d2 0%, #b8b8b8 40%, var(--photo-mid) 65%, var(--photo-dark) 100%);
  }

  .intro { position: absolute; left: 153px; top: 196px; width: 452px; }
  .intro-title {
    font-family: 'Tinos', 'Times New Roman', serif; font-weight: 700; font-size: 37px;
    color: var(--ink); line-height: 1.1; padding-bottom: 6px;
    border-bottom: 3px solid var(--ink); width: 450px;
  }
  .intro-text {
    margin-top: 15px; font-weight: 300; font-size: 14px; line-height: 21.6px; color: var(--text-dark);
  }

  .signup-panel {
    position: absolute; left: 150px; top: 480px; width: 900px; height: 428px; background: var(--panel);
  }
  .signup-title {
    position: absolute; left: 0; top: 30px; width: 900px; text-align: center;
    font-family: 'Gelasio', Georgia, serif; font-weight: 700; font-size: 21.5px;
    line-height: 29px; color: var(--white);
  }
  .signup-divider { position: absolute; left: 253px; top: 115px; width: 394px; height: 1px; background: var(--white); }

  .field {
    position: absolute; height: 30px; background: var(--white); border: none;
    font-family: 'Roboto', Arial, sans-serif; font-style: italic; font-size: 12px;
    color: var(--field-text); padding: 8px 10px; line-height: 14px;
  }
  .field-select::after {
    content: ""; position: absolute; right: 11px; top: 9px; width: 6px; height: 6px;
    border-right: 2px solid #bbbbbb; border-bottom: 2px solid #bbbbbb; transform: rotate(45deg);
  }
  .col-a { left: 47px; width: 197px; }
  .col-b { left: 251px; width: 197px; }
  .col-wide { left: 47px; width: 401px; }
  .row-1 { top: 144px; } .row-2 { top: 181.5px; } .row-3 { top: 219px; } .row-4 { top: 256.5px; }
  .field-comments { left: 456px; top: 144px; width: 401px; height: 142.5px; }

  .submit-button {
    position: absolute; left: 309px; top: 306px; width: 282px; height: 47px;
    background: var(--accent); border-radius: 5px; display: flex; align-items: center; justify-content: center; gap: 8px;
    font-family: 'Gelasio', Georgia, serif; font-weight: 700; font-size: 15.5px; color: var(--white); letter-spacing: 0.2px;
  }
  .signup-note { position: absolute; left: 0; top: 379px; width: 900px; text-align: center; font-size: 10.5px; color: var(--white); }

  .site-footer { position: absolute; left: 0; top: 1002px; width: 1200px; height: 38px; background: var(--bar); }
  .footer-legal { position: absolute; right: 247px; top: 13px; font-size: 9.5px; color: var(--white); }
  .footer-social { position: absolute; left: 962px; top: 9px; display: flex; gap: 5px; }
  .social-dot { width: 18px; height: 18px; border-radius: 50%; background: var(--white); }
</style>
</head>
<body>
<div class="page">
  <header class="site-header">
    <div class="brand">
      <span class="brand-mark"></span>
      <span class="brand-name">The Runway Guild</span>
    </div>
    <div class="brand-slogan">The World's Largest Network of Fashion Models and Agents</div>
  </header>

  <div class="hero-photo" role="img" aria-label="Black and white fashion photograph of a model seated, posed on the right side of the page"></div>

  <section class="intro">
    <h1 class="intro-title">Get Found &amp; Become a Star!</h1>
    <p class="intro-text">The Runway Guild is an agency with one of the largest networks of fashion professionals that are looking for new modeling talent. We host professional profiles for aspiring models, professional fashion models seeking work, modeling talent seekers, and top modeling agencies. We connect aspiring models with the top modeling agencies in the United States and abroad.</p>
  </section>

  <section class="signup-panel">
    <h2 class="signup-title">Instantly contact hundreds of modeling agents who are looking for new<br>talent and could make you a star!</h2>
    <div class="signup-divider"></div>

    <div class="field col-a row-1">First Name*</div>
    <div class="field col-b row-1">Last Name*</div>
    <div class="field field-select col-a row-2">Age</div>
    <div class="field col-b row-2">Zip Code</div>
    <div class="field col-wide row-3">Email Address*</div>
    <div class="field col-a row-4">Daytime Phone</div>
    <div class="field col-b row-4">Evening Phone</div>
    <div class="field field-comments">Comments</div>

    <div class="submit-button">SUBMIT YOUR PROFILE
      <svg width="10" height="12" viewBox="0 0 10 12" aria-hidden="true"><path d="M2 1.5 L7 6 L2 10.5" fill="none" stroke="#ffffff" stroke-width="2.6"/></svg>
    </div>
    <p class="signup-note">You will have the opportunity to upload photo(s) and provide other pertinent information in next step.</p>
  </section>

  <footer class="site-footer">
    <div class="footer-legal">Terms of Use &nbsp;/&nbsp; ©2013 The Runway Guild.</div>
    <div class="footer-social">
      <span class="social-dot"></span><span class="social-dot"></span><span class="social-dot"></span><span class="social-dot"></span>
    </div>
  </footer>
</div>
</body>
</html>
```